Brenmoor Group needs a business card

I would like the card to be simple but modern and elegant.
I like black and white.
or black and gold.
we are a private finance lender and also are involved in property and property developments.

please look at the business card photos i provided i would like B.G only one one side and all the other details on the other side use fonts that tie in with my theme.

Industry/Entity Type

Finance

Contact Information for Business Card

Brenmoor Group (B.G) Callum Brenmoor M: 0418396152 E: callumbren@quivomail.com

Font styles to use
Other font styles liked:
• Use fonts that would reflect our business

Colors
000000
ffffff

Requirements
Must have
• one side of details
• other side has either B.G or Brenmoor Group like in the photos provided

```html
<!DOCTYPE html>
<html lang="en">
<head>
<meta charset="utf-8">
<title>Brenmoor Group – Business Card</title>
<link rel="stylesheet" href="https://fonts.googleapis.com/css2?family=Exo+2:wght@400;600;700&family=Saira:wght@400&display=swap">
<style>
  :root {
    --backdrop: #4b4b4b;
    --card: #000000;
    --gold: #f2a81d;
  }
  * { box-sizing: border-box; margin: 0; padding: 0; }
  html, body {
    width: 1200px;
    height: 796px;
    overflow: hidden;
    background: var(--backdrop);
  }
  .stage {
    position: relative;
    width: 1200px;
    height: 796px;
  }
  .card {
    position: absolute;
    top: 128px;
    width: 330px;
    height: 540px;
    background: var(--card);
    box-shadow: 0 10px 24px rgba(0,0,0,0.45);
    color: var(--gold);
  }
  .card--front { left: 230px; }
  .card--back  { left: 640px; }

  .monogram {
    position: absolute;
    top: 120px;
    left: 0;
    width: 100%;
    text-align: center;
    font-family: "Saira", sans-serif;
    font-weight: 400;
    font-size: 72px;
    letter-spacing: 2px;
  }

  .brand-name {
    position: absolute;
    top: 52px;
    left: 0;
    width: 100%;
    text-align: center;
    font-family: "Exo 2", sans-serif;
    font-weight: 700;
    font-size: 34px;
    line-height: 1;
  }

  .details {
    position: absolute;
    left: 28px;
    right: 28px;
    top: 318px;
    font-family: "Exo 2", sans-serif;
  }
  .details__name {
    text-align: center;
    font-weight: 700;
    font-size: 29px;
    letter-spacing: 1px;
    padding-bottom: 12px;
  }
  .details__rule {
    height: 1.5px;
    background: var(--gold);
  }
  .details__phone {
    text-align: center;
    font-weight: 400;
    font-size: 22px;
    letter-spacing: 2px;
    padding: 12px 0;
  }
  .details__email {
    text-align: center;
    font-weight: 400;
    font-size: 20px;
    padding-top: 12px;
  }
</style>
</head>
<body>
<main class="stage">
  <section class="card card--front" aria-label="Card front">
    <div class="monogram">B.G</div>
  </section>

  <section class="card card--back" aria-label="Card back">
    <div class="brand-name">Brenmoor Group</div>
    <div class="details">
      <div class="details__name">Callum Brenmoor</div>
      <div class="details__rule"></div>
      <div class="details__phone">0418-396-152</div>
      <div class="details__rule"></div>
      <div class="details__email">callumbren@quivomail.com</div>
    </div>
  </section>
</main>
</body>
</html>
```